Orthopaedic Clinic Needs facebook page

Orthopaedic Clinic needs facebook page. The name of our clinic is Maple & Ridge Orthopaedics. We focus on hip and knee orthopaedic conditions, as well as general orthopaedics. The main services are total knee replacements, total hip replacements, sports injury of the knee, hip fractures. Unique selling points of our service would be 1. Patient Centred Care, 2. Value Driven, 3. 2 Double-Fellowship Trained Surgeons.

Colour scheme should fit the logo design and be within the general colour recommendations of a medical clinic.

The design should be modern, eye catching, draws the end user to the website.

We would like to design our facebook page for future social media marketing.
In accordance with local advertisement regulations pertaining to medical clinics, no statements must have any information or laudatory statements such as the use of best, better, breakthrough, champions, or any statements that imply superiority and that may create unjustified expectations of services.

Target Market(s)

Patients
Friends family and relatives of patients.

Font styles to use
Serif
Sans Serif

Requirements
Must have
• My project must have my logo.

A nice colour scheme comfortable to the eye.
Nice to have
• Nice eye catching design that will draw the end user to the page.
Should not have
• Must not have any information that create unjustified expectaions.
Must not contain laudatory statements such as best, better, breakthrough, champions, or other statement that may create unjustified expecation of services.

```html
<!DOCTYPE html>
<html lang="en">
<head>
<meta charset="utf-8">
<title>Maple &amp; Ridge Orthopaedics – Cover</title>
<link href="https://fonts.googleapis.com/css2?family=Roboto+Condensed:wght@400;500;700&display=swap" rel="stylesheet">
<style>
  :root {
    --bg-deep: #0b1a20;
    --bg-mid: #12303a;
    --bg-right: #163841;
    --teal: #5cb6b0;
    --teal-bright: #6fd3d0;
    --band-text: #0f2830;
    --white: #ffffff;
    --glow-red: #b3263a;
  }
  * { margin: 0; padding: 0; box-sizing: border-box; }
  html, body {
    width: 1200px;
    height: 457px;
    overflow: hidden;
    background: var(--bg-deep);
  }
  .cover {
    position: relative;
    width: 1200px;
    height: 457px;
    overflow: hidden;
    font-family: "Roboto Condensed", "Arial Narrow", sans-serif;
    background: linear-gradient(90deg, var(--bg-deep) 0%, var(--bg-mid) 60%, var(--bg-right) 100%);
  }
  .hero-visual {
    position: absolute;
    left: 0;
    top: 0;
    width: 760px;
    height: 396px;
    background:
      radial-gradient(circle at 250px 110px, rgba(179, 38, 58, 0.55) 0, rgba(179, 38, 58, 0) 70px),
      radial-gradient(ellipse 120px 260px at 170px 260px, rgba(111, 211, 208, 0.35) 0, rgba(111, 211, 208, 0) 100%),
      radial-gradient(ellipse 170px 230px at 490px 270px, rgba(150, 120, 100, 0.45) 0, rgba(150, 120, 100, 0) 100%),
      linear-gradient(90deg, rgba(11, 26, 32, 0) 70%, rgba(18, 48, 58, 1) 100%);
  }
  .callout {
    position: absolute;
    left: 0;
    top: 0;
  }
  .brand {
    position: absolute;
    left: 720px;
    top: 22px;
    display: flex;
    align-items: center;
    gap: 16px;
    color: var(--white);
    font-weight: 400;
  }
  .brand-mark {
    width: 74px;
    height: 74px;
    background: var(--teal);
    flex: none;
  }
  .brand-name {
    line-height: 1;
    text-transform: uppercase;
  }
  .brand-name .line-1 { display: block; font-size: 46px; letter-spacing: 1px; }
  .brand-name .line-2 { display: block; font-size: 28px; letter-spacing: 7.5px; margin-top: 6px; }
  .services {
    position: absolute;
    left: 760px;
    top: 180px;
    list-style: none;
  }
  .services li {
    display: flex;
    align-items: center;
    height: 44px;
    color: var(--white);
    font-size: 22px;
    font-weight: 500;
    letter-spacing: 0.3px;
    text-transform: uppercase;
  }
  .services svg { width: 14px; height: 20px; margin-right: 22px; flex: none; }
  .values-band {
    position: absolute;
    left: 0;
    bottom: 0;
    width: 1200px;
    height: 61px;
    background: var(--teal);
    border-top: 2px solid rgba(255, 255, 255, 0.35);
    display: flex;
    align-items: center;
    justify-content: flex-end;
    padding-right: 22px;
  }
  .values {
    color: var(--band-text);
    font-size: 23px;
    font-weight: 700;
    letter-spacing: 0.2px;
    text-transform: uppercase;
    white-space: nowrap;
  }
  .values .sep { margin: 0 10px; font-weight: 400; }
</style>
</head>
<body>
  <main class="cover">
    <div class="hero-visual" role="img" aria-label="Glowing teal wireframe leg beside a photograph of a person holding their knee with an x-ray overlay of the knee joint"></div>

    <svg class="callout" width="940" height="200" viewBox="0 0 940 200" aria-hidden="true">
      <line x1="268" y1="126" x2="936" y2="126" stroke="#ffffff" stroke-width="2"/>
      <circle cx="268" cy="126" r="15" fill="none" stroke="#ffffff" stroke-width="3"/>
      <circle cx="268" cy="126" r="8" fill="#ffffff"/>
    </svg>

    <header class="brand">
      <span class="brand-mark" aria-hidden="true"></span>
      <h1 class="brand-name">
        <span class="line-1">Maple &amp; Ridge</span>
        <span class="line-2">Orthopaedics</span>
      </h1>
    </header>

    <ul class="services">
      <li><svg viewBox="0 0 14 20" aria-hidden="true"><polyline points="3,2 11,10 3,18" fill="none" stroke="#5cb6b0" stroke-width="3.5"/></svg>Total Knee Replacements</li>
      <li><svg viewBox="0 0 14 20" aria-hidden="true"><polyline points="3,2 11,10 3,18" fill="none" stroke="#5cb6b0" stroke-width="3.5"/></svg>Total Hip Replacements</li>
      <li><svg viewBox="0 0 14 20" aria-hidden="true"><polyline points="3,2 11,10 3,18" fill="none" stroke="#5cb6b0" stroke-width="3.5"/></svg>Sports Knee Injury</li>
      <li><svg viewBox="0 0 14 20" aria-hidden="true"><polyline points="3,2 11,10 3,18" fill="none" stroke="#5cb6b0" stroke-width="3.5"/></svg>Hip Fractures</li>
    </ul>

    <footer class="values-band">
      <p class="values">Patient Centred Care<span class="sep">|</span>Value Driven<span class="sep">|</span>Double-Fellowship Trained Surgeons</p>
    </footer>
  </main>
</body>
</html>
```